Boutique custom software development company needs new business card

Our nearly 20 year old custom software development company would like to better include the fact that we are now providing Bitcoin services. These new services are B2B include education (how to acquire and securely hold Bitcoin) and integrating Bitcoin payments into existing ecommerce sites or other existing systems. Please keep the card clean and simple. Attached is our current design and some other files. vexalon.example

Target Market(s)

businesses owners interested in long term relationship

Industry/Entity Type

Custom software development and Bitcoin

Contact Information for Business Card

Marcus Ellwood, marcus@vexalon.example, vexalon.example, (888) 555-VEXAL

Font styles to use
Other font styles liked:
• monospace

Requirements
Must have
• double-sided
Nice to have
• clean and simple
Should not have
• physical address

```html
<!DOCTYPE html>
<html lang="en">
<head>
<meta charset="utf-8">
<title>Vexalon — Business Card</title>
<link href="https://fonts.googleapis.com/css2?family=Montserrat:wght@400;500;700;800&family=Open+Sans:wght@400;600&family=Great+Vibes&display=swap" rel="stylesheet">
<style>
  :root {
    --stage: #2b2d31;
    --card-white: #f4f4f2;
    --card-grey: #dcdcdb;
    --mark-faint: #ececeb;
    --orange: #ec7624;
    --blue: #3173bf;
    --ink: #1c1c1c;
    --white: #ffffff;
  }
  * { margin: 0; padding: 0; box-sizing: border-box; }
  html, body { width: 1200px; height: 1066px; overflow: hidden; }
  body {
    background: var(--stage);
    font-family: "Montserrat", sans-serif;
    position: relative;
  }

  .card {
    position: absolute;
    background: var(--card-white);
    overflow: hidden;
    box-shadow: 0 14px 30px rgba(0,0,0,.35);
  }

  /* Front side (portrait) */
  .card--front {
    left: 150px; top: 285px;
    width: 310px; height: 500px;
  }
  .front__upper {
    position: absolute; left: 0; top: 0;
    width: 100%; height: 300px;
    background: var(--card-grey);
    overflow: hidden;
  }
  .front__decor-name {
    position: absolute;
    left: 185px; top: 10px;
    font-family: "Montserrat", sans-serif;
    font-weight: 800;
    font-size: 96px;
    line-height: 1;
    color: var(--mark-faint);
    transform: rotate(62deg);
    transform-origin: left top;
    white-space: nowrap;
    letter-spacing: 2px;
  }
  .front__corner { position: absolute; left: 0; top: 0; }
  .front__phone {
    position: absolute;
    left: 50px; top: 88px;
    transform: rotate(90deg);
    transform-origin: left top;
    font-family: "Montserrat", sans-serif;
    font-weight: 500;
    font-size: 15px;
    letter-spacing: 1px;
    color: var(--ink);
    white-space: nowrap;
  }
  .front__name {
    position: absolute;
    left: 0; width: 100%; top: 352px;
    text-align: center;
    font-family: "Montserrat", sans-serif;
    font-weight: 800;
    font-size: 48px;
    letter-spacing: -1px;
    color: var(--blue);
  }
  .front__tagline {
    position: absolute;
    left: 0; width: 100%; top: 420px;
    text-align: center;
    font-family: "Open Sans", sans-serif;
    font-size: 15.5px;
    color: var(--blue);
  }
  .front__services {
    position: absolute;
    left: 0; width: 100%; top: 446px;
    text-align: center;
    font-family: "Open Sans", sans-serif;
    font-weight: 600;
    font-size: 13px;
    color: var(--orange);
  }

  /* Back side (landscape) */
  .card--back {
    left: 520px; top: 385px;
    width: 500px; height: 300px;
  }
  .back__brand {
    position: absolute;
    right: 34px; top: 40px;
    display: flex; align-items: center; gap: 10px;
  }
  .back__brand-square {
    width: 26px; height: 26px;
    background: var(--blue);
  }
  .back__brand-name {
    font-family: "Montserrat", sans-serif;
    font-weight: 700;
    font-size: 26px;
    color: var(--blue);
    letter-spacing: 1px;
  }
  .back__site {
    position: absolute;
    right: 34px; top: 78px;
    font-family: "Montserrat", sans-serif;
    font-weight: 700;
    font-size: 13px;
    color: var(--blue);
  }
  .back__signature {
    position: absolute;
    left: 140px; top: 138px;
    font-family: "Great Vibes", cursive;
    font-size: 50px;
    color: var(--ink);
    white-space: nowrap;
  }
  .back__email {
    position: absolute;
    left: 165px; top: 210px;
    font-family: "Montserrat", sans-serif;
    font-size: 14px;
    letter-spacing: 1.2px;
    color: var(--ink);
  }
  .back__corner { position: absolute; left: 0; bottom: 0; }
</style>
</head>
<body>

  <section class="card card--front" aria-label="Business card front">
    <div class="front__upper">
      <div class="front__decor-name" aria-hidden="true">VEXALON</div>
    </div>
    <svg class="front__corner" width="110" height="100" viewBox="0 0 110 100" aria-hidden="true">
      <polygon points="0,0 90,0 110,32 0,100" fill="var(--orange)"/>
      <rect x="36" y="38" width="22" height="22" fill="var(--white)"/>
      <path d="M41 54 c3 -7 7 -10 12 -11 l1 3 -3 2 c-2 1 -4 3 -5 6 l-2 1 z" fill="var(--orange)"/>
    </svg>
    <div class="front__phone">(888) 555-VEXAL</div>
    <div class="front__name">VEXALON</div>
    <div class="front__tagline">developer of custom applications</div>
    <div class="front__services">Bitcoin education &amp; payment integration</div>
  </section>

  <section class="card card--back" aria-label="Business card back">
    <div class="back__brand">
      <span class="back__brand-square"></span>
      <span class="back__brand-name">VEXALON</span>
    </div>
    <div class="back__site">vexalon.example</div>
    <div class="back__signature">Marcus Ellwood</div>
    <div class="back__email">marcus@vexalon.example</div>
    <svg class="back__corner" width="150" height="100" viewBox="0 0 150 100" aria-hidden="true">
      <polygon points="0,100 150,100 45,0 0,40" fill="var(--orange)"/>
      <g fill="none" stroke="var(--white)" stroke-width="1.8">
        <circle cx="45" cy="62" r="12"/>
        <ellipse cx="45" cy="62" rx="5" ry="12"/>
        <line x1="33" y1="62" x2="57" y2="62"/>
        <line x1="35" y1="55" x2="55" y2="55"/>
        <line x1="35" y1="69" x2="55" y2="69"/>
      </g>
    </svg>
  </section>

</body>
</html>
```